Design a Restaurant Menu for Modern Japanese Restaurant

Please design a Restaurant Menu for Modern Japanese Restaurant.
Following is the sample menu design.
No need to be similar with sample design, but prefer with this layout
(of cause you can change around the layout)
First page
https://www.quillvault.com/s/mr7pk2zqe55wbnj/top_menu_first_page.pdf?dl=0
Secand and Third page
https://www.quillvault.com/s/hgs3ruyw82cfq0t/Secand_and%20Third_page.doc?dl=0
Last page
https://www.quillvault.com/s/wzt6mlpa19xjkrb/Last_page.doc?dl=0
total 4 pages with A4 size. (like a 2 page book)
design taste: Simple, conspicuous, easy viewing.
you can use any photo from the following link and website.
photo link
https://www.quillvault.com/sh/k42mnbzrtqu8e/BBHTQrvLmPgWsaYuDeNhT47kd?dl=0
Website
http://tallowreedkitchen.com.au/4/TALLOW_REED_KITCHEN-TOP.html

```html
<!DOCTYPE html>
<html lang="en">
<head>
<meta charset="utf-8">
<title>Tallow Reed Kitchen — Menu Cover</title>
<link rel="stylesheet" href="https://fonts.googleapis.com/css2?family=Cinzel+Decorative:wght@400&family=Poiret+One&display=swap">
<style>
  :root {
    --backdrop: #d4d4d4;
    --cover-black: #050404;
    --peach: #ecc3a6;
    --room-warm: #8a6a4a;
    --room-dark: #1a120c;
  }
  * { margin: 0; padding: 0; box-sizing: border-box; }
  html, body {
    width: 1200px;
    height: 800px;
    overflow: hidden;
    background: var(--backdrop);
  }
  .stage {
    position: relative;
    width: 1200px;
    height: 800px;
    display: flex;
    align-items: center;
    justify-content: center;
  }
  .menu-cover {
    position: relative;
    width: 509px;
    height: 720px;
    background: var(--cover-black);
    box-shadow: 0 12px 30px rgba(0,0,0,0.25);
    display: flex;
    flex-direction: column;
    align-items: center;
  }
  .menu-title {
    margin-top: 62px;
    font-family: "Cinzel Decorative", serif;
    font-weight: 400;
    font-size: 92px;
    line-height: 1;
    letter-spacing: -2px;
    color: var(--peach);
  }
  .dining-photo {
    margin-top: 70px;
    width: 150px;
    height: 196px;
    border-radius: 10px;
    background:
      radial-gradient(ellipse at 45% 62%, rgba(230,200,170,0.75) 0%, rgba(138,106,74,0.55) 30%, rgba(26,18,12,0) 70%),
      linear-gradient(180deg, #3a2e22 0%, var(--room-warm) 45%, var(--room-dark) 100%);
    box-shadow: 0 0 18px 10px var(--cover-black) inset;
  }
  .cover-tagline {
    margin-top: 58px;
    list-style: none;
    text-align: center;
    font-family: "Poiret One", sans-serif;
    font-size: 31px;
    line-height: 1.75;
    color: var(--peach);
  }
</style>
</head>
<body>
  <main class="stage">
    <article class="menu-cover">
      <h1 class="menu-title">Menu</h1>
      <div class="dining-photo" role="img" aria-label="Dimly lit restaurant dining table set with glasses and a candle"></div>
      <ul class="cover-tagline">
        <li>Tallow Reed Kitchen</li>
        <li>Contemporary</li>
        <li>Australian / Japanese</li>
      </ul>
    </article>
  </main>
</body>
</html>
```